Labels design for a a range of food products

We are looking for labels design for a range of food product. The design should be the same for all the label with brown/black background and gold and white wording like the one attached.
The size and the content of the label will change depending on the different products.
I have also attached the logo to be used which is the logo "CORVANE" Telmora. You shall be using the black and gold version. Brighter/shining gold is better.
The first label to be designed is the one related a plastic tray like the one Cappelletti" file: IMG_20151231_021838
The second label to be designed is the one related to a bottle like the one "Olive Oil" file; IMG_20151231_021651
The third label to be designed is the one related to a jar like the one "Olive Taggiasche" file: IMG_20151231_021531 and IMG_20151231_021549
The fourth label to be designed is the one related to bag like the one IMG_20151231_021506
The fifth label to be designed is the one related to the bottle. IMG_20151231_021426_panorama
This files are only samples. I have attached a file excel "Texts for Labels" in which you will find the text to be applied for the labels.
In order to decide the best design a front and a back label should be provided.

Food Consumers

Product

• Front and Back Label
• Some pictures of the product on the label would be nice to have to recall what is inside.

```html
<!DOCTYPE html>
<html lang="it">
<head>
<meta charset="utf-8">
<title>CORVANE Telmora – Etichette Olio Extravergine</title>
<link href="https://fonts.googleapis.com/css2?family=Playfair+Display:wght@400;700&family=Great+Vibes&family=Kalam:wght@400&display=swap" rel="stylesheet">
<style>
  :root {
    --bg-dark: #14110a;
    --bg-mid: #3a3424;
    --label-black: #0b0806;
    --frame-yellow: #f2d41a;
    --gold: #d9a640;
    --gold-light: #f0c766;
    --cream: #f3ead6;
    --wine: #4a0d0d;
    --red-small: #8a1c1c;
    --olive: #6f7a22;
  }
  * { margin: 0; padding: 0; box-sizing: border-box; }
  html, body { width: 1200px; height: 771px; overflow: hidden; }
  body {
    background: radial-gradient(ellipse at 50% 40%, var(--bg-mid) 0%, var(--bg-dark) 75%);
    font-family: "Playfair Display", serif;
    display: flex; justify-content: center; align-items: center; gap: 120px;
  }
  .label {
    width: 190px; height: 690px;
    background: var(--label-black);
    border: 3px solid var(--frame-yellow);
    padding: 6px;
    box-shadow: 0 0 40px rgba(0,0,0,.6);
  }
  .label__inner {
    width: 100%; height: 100%;
    border: 1px solid var(--gold);
    display: flex; flex-direction: column; align-items: center;
    padding: 22px 14px 14px;
    color: var(--cream);
    text-align: center;
  }
  .brand { display: flex; flex-direction: column; align-items: center; gap: 6px; }
  .brand__dot { width: 46px; height: 46px; border-radius: 50%; background: var(--gold); }
  .brand__name { color: var(--gold-light); font-size: 15px; font-weight: 700; line-height: 1.15; letter-spacing: .5px; }
  .front__type { margin-top: 42px; font-size: 9px; line-height: 1.4; }
  .front__area { margin-top: 10px; font-size: 9px; font-weight: 700; }
  .front__olives {
    margin-top: 30px; width: 70px; height: 52px; border-radius: 50%;
    background: radial-gradient(circle at 50% 55%, var(--olive) 0%, #3b2410 55%, transparent 75%);
  }
  .front__method { margin-top: 18px; font-family: "Great Vibes", cursive; color: var(--frame-yellow); font-size: 20px; }
  .front__desc {
    margin-top: 40px; font-family: "Great Vibes", cursive; font-size: 16px; line-height: 1.45;
    color: var(--cream); opacity: .85; padding: 0 6px;
  }
  .front__volume { margin-top: auto; font-size: 10px; align-self: flex-start; padding-left: 18px; }
  .back__maker { font-family: "Kalam", cursive; font-size: 12px; line-height: 1.65; text-align: left; }
  .back__seal { margin-top: 34px; }
  .back__note { margin-top: 26px; font-size: 7.5px; line-height: 1.45; color: var(--cream); opacity: .85; }
  .back .brand { margin-top: 16px; gap: 4px; }
  .back .brand__dot { width: 22px; height: 22px; }
  .back .brand__name { font-size: 8px; }
  .back__storage {
    margin-top: 14px; width: 120px; padding: 6px 8px;
    background: var(--wine); border: 1px solid var(--cream);
    font-size: 7.5px; font-weight: 700; line-height: 1.35;
  }
  .back__batch { margin-top: auto; font-size: 6px; color: var(--red-small); }
</style>
</head>
<body>
  <section class="label front" aria-label="Etichetta frontale">
    <div class="label__inner">
      <div class="brand">
        <span class="brand__dot"></span>
        <span class="brand__name">CORVANE<br>Telmora</span>
      </div>
      <p class="front__type">Olio Extravergine di Oliva</p>
      <p class="front__area">Collina di Varenzo</p>
      <div class="front__olives" role="img" aria-label="Foto di un rametto con olive verdi"></div>
      <p class="front__method">Estratto a freddo</p>
      <p class="front__desc">Olio di Oliva di categoria superiore ottenuto direttamente dalle olive e unicamente mediante procedimenti meccanici.</p>
      <p class="front__volume">750ML</p>
    </div>
  </section>

  <section class="label back" aria-label="Etichetta posteriore">
    <div class="label__inner">
      <p class="back__maker">Prodotto e imbottigliato all'origine per VELNARI S.r.l. - C.da Morena 4/B Torlano (TL) - Italy nello stabilimento di Via dei Pini 27/A Torlano (TL)</p>
      <svg class="back__seal" width="52" height="52" viewBox="0 0 52 52" aria-hidden="true">
        <circle cx="26" cy="26" r="23" fill="none" stroke="var(--cream)" stroke-width="1.5"/>
      </svg>
      <p class="back__note">L'olio extravergine di oliva a cui viene riconosciuto il marchio DOP a tutela e garanzia del consumatore ha superato tutti i controlli di laboratorio e di prove di assaggio (PANEL TEST) operate da strutture esterne alla produzione</p>
      <div class="brand">
        <span class="brand__dot"></span>
        <span class="brand__name">CORVANE Telmora</span>
      </div>
      <p class="back__storage">Modalità di conservazione: Conservare in luogo fresco, al riparo dalla luce e da fonti di calore</p>
      <p class="back__batch">Lotto e scadenza vedi tappo</p>
    </div>
  </section>
</body>
</html>
```